IT Company needs full suite of stationery

Our company 4027 Veltrane Partners Inc. is an IT company based in Toronto, Canada. Based on our logo we would like to see business cards(front and back), letterhead, envelope, brochure template. Design would be simple, not too bright, modern but can be used for many years, good theme throughout. Our official logo is the the fullcolor_a, full company name is 4027 Veltrane Partners Inc., Please include full company name on all pieces. Logo can be modified to be the graphic only with the "4027 Partners", I have cropped it myself for a couple files but I am no designer. We will provide lots of feedback so post early and often.
Updates

Reason: Very busy around the holidays, like a lot of the designs currently submitted, will definitely be picking one. Thanks for your submissions and merry Christmas and Happy New Year to everyone.

Industry/Entity Type

Business

```html
<!DOCTYPE html>
<html lang="en">
<head>
<meta charset="utf-8">
<title>4027 Veltrane Partners Inc. — Business Cards</title>
<link href="https://fonts.googleapis.com/css2?family=Open+Sans:wght@400;600;700&display=swap" rel="stylesheet">
<style>
  :root {
    --backdrop: #3a3431;
    --card: #151515;
    --card-edge: #222;
    --green: #3dba3f;
    --silver: #a9aaad;
    --text-grey: #b9b9b9;
    --emboss: #1d1d1d;
  }
  * { margin: 0; padding: 0; box-sizing: border-box; }
  html, body { width: 1200px; height: 716px; overflow: hidden; }
  body {
    background: var(--backdrop);
    font-family: "Open Sans", Arial, sans-serif;
    position: relative;
  }
  .card {
    position: absolute;
    top: 210px;
    width: 520px;
    height: 297px;
    background: var(--card);
    border: 1px solid var(--card-edge);
    border-radius: 3px;
    box-shadow: 0 10px 28px rgba(0,0,0,.45);
  }
  .card-front { left: 50px; }
  .card-back { left: 630px; }

  .brand { display: flex; align-items: center; gap: 14px; }
  .brand-dot { width: 58px; height: 58px; border-radius: 50%; flex: none; }
  .brand-name { font-weight: 700; font-size: 34px; letter-spacing: 1px; white-space: nowrap; }

  .card-front .brand {
    position: absolute; left: 50%; top: 50%;
    transform: translate(-50%, -50%);
  }
  .card-front .brand-dot { background: var(--emboss); width: 84px; height: 84px; }
  .card-front .brand-name { color: var(--silver); font-size: 38px; }

  .card-back .brand { position: absolute; left: 28px; top: 52px; gap: 10px; }
  .card-back .brand-dot { background: var(--green); width: 46px; height: 46px; }
  .card-back .brand-name { color: var(--silver); font-size: 22px; }

  .contact {
    position: absolute; left: 268px; top: 48px;
    color: var(--text-grey); font-size: 12px; line-height: 1.35;
  }
  .person-name { color: var(--green); font-weight: 700; font-size: 17px; line-height: 1.2; }
  .person-role { font-size: 12px; margin-bottom: 12px; }
  .company { color: var(--green); font-weight: 700; font-size: 11.5px; }
  .address { margin-bottom: 14px; }
  .lines { list-style: none; }
  .lines li { display: flex; align-items: center; gap: 8px; height: 18px; }
  .lines svg { width: 11px; height: 11px; flex: none; fill: var(--green); }
</style>
</head>
<body>
  <section class="card card-front" aria-label="Business card front">
    <div class="brand">
      <span class="brand-dot"></span>
      <span class="brand-name">4027 Partners</span>
    </div>
  </section>

  <section class="card card-back" aria-label="Business card back">
    <div class="brand">
      <span class="brand-dot"></span>
      <span class="brand-name">4027 Partners</span>
    </div>
    <div class="contact">
      <p class="person-name">Marek Odell</p>
      <p class="person-role">President</p>
      <p class="company">4027 Veltrane Partners Inc.</p>
      <p class="address">88 Calder Lane<br>Suite 305 Toronto</p>
      <ul class="lines">
        <li><svg viewBox="0 0 12 12"><path d="M2.5 1h2l1 3-1.4 1a6 6 0 0 0 3 3l1-1.4 3 1v2c0 .6-.4 1-1 1A10 10 0 0 1 1.5 2c0-.6.4-1 1-1z"/></svg>+123-555-0147</li>
        <li><svg viewBox="0 0 12 12"><rect x="3" y="0.5" width="6" height="11" rx="1"/></svg>+123-555-0147</li>
        <li><svg viewBox="0 0 12 12"><rect x="0.5" y="2" width="11" height="8" rx="1"/></svg>info@4027partners.com</li>
        <li><svg viewBox="0 0 12 12"><circle cx="6" cy="6" r="5.5"/></svg>www.4027partners.com</li>
      </ul>
    </div>
  </section>
</body>
</html>
```